Tallowmere Nourish

We are a nutritional coaching business who specalise in:

Weight Loss
Improved Body Composition
Personalised Meal Plans
Health & Vitality

We are in the process of developing a facebook page and need a cover photo design. Our logo has already been created which we will use for the profile pic. We would like the background to be simple and include our logo as well as the 4 dot points above.

Project Deadline Extended Reason: Going to commit the funds nows everyone, however would just like to extend the time frame only for a short period to get more designs. Added Friday, January 09, 2015

• Please make sure the design will upload easily to facebook, specifically the cover photo and not become distorted.

```html
<!DOCTYPE html>
<html lang="en">
<head>
<meta charset="utf-8">
<title>Tallowmere Nourish – Facebook Cover and Profile Image</title>
<link href="https://fonts.googleapis.com/css2?family=Open+Sans:wght@400;600&family=Roboto+Slab:wght@700&display=swap" rel="stylesheet">
<style>
  :root{
    --page-bg:#e9e7e3;
    --card-bg:#f4f4f3;
    --white:#ffffff;
    --ink-grey:#55595c;
    --body-grey:#5e6266;
    --brand-green:#6cb33f;
    --brand-blue:#2b6cb3;
    --photo-red:#c8352a;
    --photo-teal:#0f8d7c;
    --photo-green:#7aa84a;
  }
  *{box-sizing:border-box;margin:0;padding:0}
  html,body{width:1200px;height:889px;overflow:hidden}
  body{background:var(--page-bg);position:relative;font-family:"Open Sans",Arial,sans-serif}

  .profile-image{
    position:absolute;left:42px;top:306px;width:232px;height:232px;
    background:var(--white);box-shadow:0 2px 6px rgba(0,0,0,.18);
    display:flex;align-items:center;justify-content:center;
  }
  .brand-name{
    display:flex;align-items:center;gap:8px;
    font-family:"Open Sans",Arial,sans-serif;font-weight:600;color:var(--brand-blue);
    white-space:nowrap;
  }
  .brand-name .dot{width:12px;height:12px;border-radius:50%;background:var(--brand-blue);flex:none}
  .profile-image .brand-name{font-size:21px}

  .cover{
    position:absolute;left:302px;top:266px;width:856px;height:316px;
    background:var(--card-bg);box-shadow:0 2px 8px rgba(0,0,0,.2);overflow:hidden;
  }
  .cover .brand-name{position:absolute;left:64px;top:30px;font-size:26px}
  .cover-photo{
    position:absolute;left:0;top:78px;width:560px;height:238px;
    background:
      radial-gradient(ellipse at 22% 55%, var(--photo-red) 0%, rgba(200,53,42,0) 42%),
      radial-gradient(ellipse at 66% 48%, var(--photo-teal) 0%, rgba(15,141,124,0) 48%),
      linear-gradient(100deg, var(--photo-green) 0%, #d9c24a 22%, #e8e6e2 88%, var(--card-bg) 100%);
    -webkit-mask-image:linear-gradient(90deg,#000 80%,transparent 100%);
            mask-image:linear-gradient(90deg,#000 80%,transparent 100%);
  }
  .cover-copy{position:absolute;left:555px;top:26px;width:290px}
  .headline{
    font-family:"Roboto Slab",Georgia,serif;font-weight:700;font-size:29px;line-height:30px;
    color:var(--ink-grey);
  }
  .headline .accent{color:var(--brand-green)}
  .services{list-style:none;margin-top:14px}
  .services li{
    display:flex;align-items:center;gap:8px;
    font-size:16px;line-height:25px;color:var(--body-grey);
  }
  .services svg{flex:none}
</style>
</head>
<body>

  <div class="profile-image">
    <div class="brand-name"><span class="dot"></span>Tallowmere Nourish</div>
  </div>

  <section class="cover">
    <div class="brand-name"><span class="dot"></span>Tallowmere Nourish</div>
    <div class="cover-photo" role="img" aria-label="Photo of fresh vegetables, a red apple wrapped in a tape measure and a pair of teal dumbbells"></div>

    <div class="cover-copy">
      <h1 class="headline">Helping you<br>transform through<br><span class="accent">healthy diet</span><br>and <span class="accent">exercise</span></h1>
      <ul class="services">
        <li><svg width="18" height="18" viewBox="0 0 18 18" aria-hidden="true"><circle cx="9" cy="9" r="7.5" fill="none" stroke="#6cb33f" stroke-width="1.8"/><path d="M5.3 9.3l2.4 2.4 5-5" fill="none" stroke="#6cb33f" stroke-width="1.8" stroke-linecap="round" stroke-linejoin="round"/></svg>Weight Loss</li>
        <li><svg width="18" height="18" viewBox="0 0 18 18" aria-hidden="true"><circle cx="9" cy="9" r="7.5" fill="none" stroke="#6cb33f" stroke-width="1.8"/><path d="M5.3 9.3l2.4 2.4 5-5" fill="none" stroke="#6cb33f" stroke-width="1.8" stroke-linecap="round" stroke-linejoin="round"/></svg>Improved Body Composition</li>
        <li><svg width="18" height="18" viewBox="0 0 18 18" aria-hidden="true"><circle cx="9" cy="9" r="7.5" fill="none" stroke="#6cb33f" stroke-width="1.8"/><path d="M5.3 9.3l2.4 2.4 5-5" fill="none" stroke="#6cb33f" stroke-width="1.8" stroke-linecap="round" stroke-linejoin="round"/></svg>Health and Vitality</li>
      </ul>
    </div>
  </section>

</body>
</html>
```